BM banner

we need a banner design (36"x120" horizontal) that will be displayed on a local high school baseball field. My company ( Quill Pennant Co) has been producing signage for the Birch Meadows community since 2009. We would like to communicate that we do more than banners. The final design should include the slogan "Signs Shirts Swag" and our Logo.

Target Market(s)

companies, teams, events, shirt and other marketing items.

Industry/Entity Type

Sign, Print,

Font styles to use
Sans Serif

Requirements
Should not have
• no baseball content.

```html
<!DOCTYPE html>
<html lang="en">
<head>
<meta charset="utf-8">
<title>Quill Pennant Co — Field Banner</title>
<link rel="stylesheet" href="https://fonts.googleapis.com/css2?family=Roboto+Condensed:wght@700&display=swap">
<style>
  :root {
    --backdrop: #8c8c8c;
    --banner-white: #ffffff;
    --ink: #000000;
    --pill-grey: #5b5b5b;
    --slogan-white: #ffffff;
  }
  html, body {
    margin: 0;
    padding: 0;
    width: 1200px;
    height: 1200px;
    overflow: hidden;
    background: var(--backdrop);
  }
  .canvas {
    position: relative;
    width: 1200px;
    height: 1200px;
    background: var(--backdrop);
    font-family: "Roboto Condensed", "Arial Narrow", sans-serif;
  }
  .banner {
    position: absolute;
    left: 63px;
    top: 437px;
    width: 1074px;
    height: 325px;
    background: var(--banner-white);
  }
  .banner__rule {
    position: absolute;
    left: 0;
    width: 100%;
    background: var(--ink);
  }
  .banner__rule--top { top: 0; height: 14px; }
  .banner__rule--bottom { bottom: 0; height: 15px; }
  .brand-name {
    position: absolute;
    left: 42px;
    top: 100px;
    width: 260px;
    margin: 0;
    color: var(--ink);
    font-weight: 700;
    font-size: 50px;
    line-height: 1.0;
    text-transform: uppercase;
  }
  .slogan-pill {
    position: absolute;
    left: 312px;
    top: 106px;
    width: 737px;
    height: 110px;
    border-radius: 55px;
    background: var(--pill-grey);
    display: flex;
    align-items: center;
    justify-content: center;
  }
  .slogan {
    margin: 0;
    color: var(--slogan-white);
    font-weight: 700;
    font-size: 76px;
    letter-spacing: 0.5px;
    line-height: 1;
    transform: translateY(-2px);
  }
</style>
</head>
<body>
  <main class="canvas">
    <section class="banner">
      <div class="banner__rule banner__rule--top"></div>
      <p class="brand-name">Quill<br>Pennant Co</p>
      <div class="slogan-pill">
        <h1 class="slogan">Signs Shirts Swag</h1>
      </div>
      <div class="banner__rule banner__rule--bottom"></div>
    </section>
  </main>
</body>
</html>
```